KMT Billboard Design Project

Tax sensitization messages. Please find attached document with the creative brief information.

Reason: Submitted designs yet be viewed by project team.

```html
<!DOCTYPE html>
<html lang="en">
<head>
<meta charset="utf-8">
<title>KMT Billboard – Tax Sensitization</title>
<link href="https://fonts.googleapis.com/css2?family=Jost:wght@400;500;600;700&family=Oswald:wght@500;600&display=swap" rel="stylesheet">
<style>
  :root {
    --navy-deep: #0c2552;
    --navy: #123a78;
    --navy-light: #1d4f96;
    --band-grey: #8f8f8f;
    --alert-red: #e3101a;
    --paper: #ffffff;
    --photo-warm: #c9a48e;
    --photo-cool: #dcdad6;
  }
  html, body {
    margin: 0;
    padding: 0;
    width: 1200px;
    height: 798px;
    overflow: hidden;
    background: var(--paper);
    font-family: "Jost", sans-serif;
  }
  .billboard {
    position: relative;
    width: 1200px;
    height: 798px;
    overflow: hidden;
  }
  .billboard-shapes,
  .photo-area {
    position: absolute;
    left: 0;
    top: 0;
  }
  .intro {
    position: absolute;
    left: 528px;
    top: 76px;
    width: 636px;
    margin: 0;
    color: var(--paper);
    font-size: 21px;
    line-height: 1.3;
    text-align: justify;
  }
  .duties {
    position: absolute;
    left: 582px;
    top: 236px;
    width: 590px;
    margin: 0;
    padding: 0;
    list-style: none;
    color: var(--paper);
    font-size: 21px;
    line-height: 1.15;
  }
  .duties li {
    display: flex;
    gap: 18px;
    margin-bottom: 22px;
  }
  .duties svg {
    flex: 0 0 19px;
    width: 19px;
    height: 19px;
    margin-top: 3px;
  }
  .hotline-title {
    position: absolute;
    left: 560px;
    top: 490px;
    width: 600px;
    margin: 0;
    color: var(--paper);
    font-size: 35px;
    font-weight: 500;
    line-height: 50px;
    white-space: nowrap;
    text-align: center;
  }
  .hotline-numbers {
    position: absolute;
    left: 550px;
    top: 560px;
    width: 630px;
    height: 100px;
    margin: 0;
    color: var(--paper);
    font-family: "Oswald", sans-serif;
    font-size: 56px;
    font-weight: 600;
    line-height: 100px;
    white-space: nowrap;
    text-align: center;
  }
  .website {
    position: absolute;
    left: 560px;
    top: 688px;
    width: 600px;
    margin: 0;
    display: flex;
    justify-content: center;
    align-items: center;
    gap: 14px;
    color: var(--paper);
    font-size: 34px;
    font-weight: 500;
    white-space: nowrap;
  }
  .website svg { width: 20px; height: 20px; }
  .brand-tag {
    position: absolute;
    left: 112px;
    top: 660px;
    width: 252px;
    height: 120px;
    background: var(--paper);
    display: flex;
    align-items: center;
    justify-content: center;
    color: var(--alert-red);
    font-size: 84px;
    font-weight: 700;
    letter-spacing: 2px;
  }
</style>
</head>
<body>
<main class="billboard">
  <svg class="billboard-shapes" width="1200" height="798" viewBox="0 0 1200 798" aria-hidden="true">
    <defs>
      <linearGradient id="panelGradient" x1="0" y1="0" x2="1" y2="1">
        <stop offset="0" stop-color="var(--navy)"/>
        <stop offset="0.55" stop-color="var(--navy-light)"/>
        <stop offset="1" stop-color="var(--navy-deep)"/>
      </linearGradient>
    </defs>
    <rect class="info-panel" x="0" y="0" width="1200" height="798" fill="url(#panelGradient)"/>
    <polygon class="summary-band" points="440,60 1200,60 1200,212 480,212" fill="var(--band-grey)"/>
    <polygon class="divider-stripe" points="0,0 444,0 571,520 444,798 0,798" fill="var(--paper)"/>
    <polygon class="red-band" points="553,560 1200,560 1200,660 512,660" fill="var(--alert-red)"/>
  </svg>

  <svg class="photo-area" width="560" height="798" viewBox="0 0 560 798" role="img" aria-label="Photo of a young couple reviewing a tax document together at a kitchen table with a laptop">
    <defs>
      <linearGradient id="photoGradient" x1="0" y1="0" x2="1" y2="1">
        <stop offset="0" stop-color="var(--photo-cool)"/>
        <stop offset="0.5" stop-color="var(--photo-warm)"/>
        <stop offset="1" stop-color="var(--photo-cool)"/>
      </linearGradient>
    </defs>
    <polygon points="0,0 409,0 543,520 416,798 0,798" fill="url(#photoGradient)"/>
  </svg>

  <p class="intro">The Kalvora Metro Treasury (KMT) is responsible to collect all revenues of the government of Kalvora. The following is a summary of key responsibilities:</p>

  <ul class="duties">
    <li><svg viewBox="0 0 20 20" aria-hidden="true"><rect x="1" y="1" width="18" height="18" fill="none" stroke="#fff" stroke-width="2"/><path d="M5 10 l4 4 l7 -9" fill="none" stroke="#fff" stroke-width="2.4"/></svg><span>Administer and enforce revenue laws in accordance with the Code and related laws.</span></li>
    <li><svg viewBox="0 0 20 20" aria-hidden="true"><rect x="1" y="1" width="18" height="18" fill="none" stroke="#fff" stroke-width="2"/><path d="M5 10 l4 4 l7 -9" fill="none" stroke="#fff" stroke-width="2.4"/></svg><span>Assess, Collect, Audit &amp; Account for all National Revenues</span></li>
    <li><svg viewBox="0 0 20 20" aria-hidden="true"><rect x="1" y="1" width="18" height="18" fill="none" stroke="#fff" stroke-width="2"/><path d="M5 10 l4 4 l7 -9" fill="none" stroke="#fff" stroke-width="2.4"/></svg><span>Facilitate legitimate Trade</span></li>
    <li><svg viewBox="0 0 20 20" aria-hidden="true"><rect x="1" y="1" width="18" height="18" fill="none" stroke="#fff" stroke-width="2"/><path d="M5 10 l4 4 l7 -9" fill="none" stroke="#fff" stroke-width="2.4"/></svg><span>Enforce Customs Border Management</span></li>
  </ul>

  <h2 class="hotline-title">CALL OUR HOTLINE NUMBERS</h2>
  <p class="hotline-numbers">0882045193/0774308256</p>

  <p class="website">
    <svg viewBox="0 0 22 22" aria-hidden="true"><circle cx="11" cy="11" r="9" fill="none" stroke="#fff" stroke-width="2"/><ellipse cx="11" cy="11" rx="4" ry="9" fill="none" stroke="#fff" stroke-width="1.6"/><line x1="2" y1="11" x2="20" y2="11" stroke="#fff" stroke-width="1.6"/></svg>
    <span>www.kmt.gov.kv</span>
  </p>

  <div class="brand-tag">KMT</div>
</main>
</body>
</html>
```